Letterhead/cards for law firm
per the logo
Project: Letterhead/cards for law firm
Letterhead/cards for law firm - Law
Creative Brief
Professional
Kemal Farouki
4826 BRIDGER FALLOW RD Brookhaven, Ohio 45871 2159 Tarrow Lane, Ste.200 Millbrook, Ohio 45612
5134829167 (cincy)
9372619038 (dayton)
kf@kflegalgroupmail.com
4826 BRIDGER FALLOW RD
we have two offices, one in Cincinnati, one in Dayton.

```html
<!DOCTYPE html>
<html lang="en">
<head>
<meta charset="utf-8">
<title>Farouki Law – Business Cards</title>
<link href="https://fonts.googleapis.com/css2?family=Open+Sans:wght@400;600;700&display=swap" rel="stylesheet">
<style>
  :root{
    --navy:#1f2466;
    --sky:#3f7fc4;
    --ink:#4a4d5a;
    --muted:#7c7f8a;
    --paper:#ffffff;
    --stage:#e9eaee;
    --rule:#c9cbd3;
  }
  *{margin:0;padding:0;box-sizing:border-box}
  html,body{width:1200px;height:914px;overflow:hidden;background:var(--stage);font-family:"Open Sans",Arial,sans-serif}
  .canvas{position:relative;width:1200px;height:914px}
  .card{position:absolute;width:700px;height:400px;border-radius:18px;overflow:hidden;box-shadow:0 10px 30px rgba(20,24,60,.18)}
  .card-back{left:60px;top:50px;background:var(--navy)}
  .card-front{left:440px;top:474px;background:var(--paper)}

  .brand{display:flex;align-items:center;gap:14px;font-weight:700;letter-spacing:.04em;white-space:nowrap}
  .brand-mark{display:block;background:currentColor}
  .card-back .brand{position:absolute;left:50%;top:50%;transform:translate(-50%,-50%);color:var(--paper);font-size:48px}
  .card-back .brand-mark{width:30px;height:30px}

  .card-front .brand{position:absolute;left:44px;top:62px;color:var(--navy);font-size:28px;gap:10px}
  .card-front .brand-mark{width:18px;height:18px}

  .holder{position:absolute;left:372px;top:40px}
  .holder-name{font-size:22px;font-weight:700;color:var(--navy)}
  .holder-title{font-size:11px;color:var(--muted);margin-top:2px}
  .divider{position:absolute;left:290px;right:0;top:108px;height:1px;background:var(--rule)}

  .offices{position:absolute;right:34px;top:128px;text-align:right;font-size:11.5px;line-height:1.55;color:var(--ink)}
  .office + .office{margin-top:8px}

  .contacts{position:absolute;left:44px;top:196px;list-style:none;font-size:12.5px;line-height:1.75;color:var(--ink)}
  .contacts li{display:flex;align-items:center;gap:8px}
  .contacts svg{width:11px;height:11px;fill:var(--navy);flex:none}

  .website{position:absolute;right:34px;top:300px;font-size:12px;color:var(--navy)}
  .swoosh{position:absolute;left:0;bottom:0;width:700px;height:80px}
</style>
</head>
<body>
<main class="canvas">
  <section class="card card-back" aria-label="Card back">
    <div class="brand"><span class="brand-mark"></span>FAROUKILAW</div>
  </section>

  <section class="card card-front" aria-label="Card front">
    <div class="brand"><span class="brand-mark"></span>FAROUKILAW</div>

    <div class="holder">
      <p class="holder-name">Kemal Farouki</p>
      <p class="holder-title">Co / Funder</p>
    </div>
    <div class="divider"></div>

    <div class="offices">
      <p class="office">4826 BRIDGER FALLOW RD<br>Brookhaven, Ohio 45871</p>
      <p class="office">2159 Tarrow Lane, Ste.310<br>Millbrook, Ohio 45612</p>
    </div>

    <ul class="contacts">
      <li><svg viewBox="0 0 10 10"><path d="M2 0h2l1 3-1.5 1a6 6 0 0 0 2.5 2.5L7 5l3 1v2c0 1-1 2-2 2A8 8 0 0 1 0 2c0-1 1-2 2-2z"/></svg>513 307 4418</li>
      <li><svg viewBox="0 0 10 10"><rect x="0" y="2" width="10" height="7" rx="1"/><rect x="2" y="0" width="6" height="3"/></svg>513 640 2281</li>
      <li><svg viewBox="0 0 10 10"><path d="M0 2h10v6H0zM0 2l5 3 5-3" stroke="#fff" stroke-width=".8"/></svg>kf@kflegalgroupmail.com</li>
      <li><svg viewBox="0 0 10 10"><rect x="2" y="0" width="6" height="10" rx="1"/></svg>937 261 9038 (dayton)</li>
      <li><svg viewBox="0 0 10 10"><rect x="2" y="0" width="6" height="10" rx="1"/></svg>513 482 9167 (cincy)</li>
    </ul>

    <p class="website">faroukilawoffices.com</p>

    <svg class="swoosh" viewBox="0 0 700 80" preserveAspectRatio="none" aria-hidden="true">
      <path d="M0 60 L330 60 C370 60 380 42 420 40 L700 34 L700 80 L0 80Z" fill="var(--sky)"/>
      <path d="M0 66 L330 66 C372 66 384 50 424 48 L700 44 L700 80 L0 80Z" fill="var(--navy)"/>
    </svg>
  </section>
</main>
</body>
</html>
```